Create our new Brightcup Coffee Syrup Label designs. A delicious job!

Design a front label for a range of coffee syrup flavours. The brand is 'Brightcup Coffee Syrups'. The flavours, vanilla, hazelnut and caramel.
Our coffee syrups are made with only natural colours and flavours and are positioned in the popular premium space in Australian and international cafes.
The labels will be applied to 750 ml Boston Bottles (see attached image).
Given that coffee syrups are often positioned in high visibility locations in cafes, they can be considered as objects of functional beauty.
This range is a sub brand for our company and I have attached our main brand images in the flavours we want. we want this brand to look different to this Marlowe branded range, but included the image to show what we are currently doing in this space.
The different flavours can be identified by a combination of colour and text, which may be a line or section of the otherwise same overall design.
We are going to do a 2 part label with the front just carrying Brand and flavour descriptors plus 750 ml.
Total Bottle height is 240 mm bottle width is 70 mm

Target Market(s)

Cafe patrons, primarily women, 18-35, Middle class in terms of economics, regular cafe patrons. Who are looking for a guilt free treat in their busy day.

Logo Text

Brightcup Coffee Syrups Vanilla (or Hazelnut, or Caramel) 750 ml

Logo styles of interest
Pictorial/Combination Logo
Font styles to use
Sans Serif

Colors

Designer to choose colors to be used in the design.

Requirements
Must have
• A clear design, which is a combination of font and image. it needs to be legible from up to 2m away (across a counter in a cafe).
• We would like to see a device, which may be a gold drop, that may be the 'brightcup' meant to the coffee.
• The way our coffee syrups are used is by adding a small amount (15 ml) to a cup
• of coffee, this adds both flavour and sweetness to the overall coffee experience, and cafes charge a premium for this service. We want our package to show this will be a great thing to do.
• We have a few options in terms of Label stock. We can print on a foil, that will allow a metallic sheen to come through the colours (see example of the Marlowe branded bottles.
Nice to have
• We are looking for a modern, clean and distinctive look and feel to this range.
• I have added a key line for the front and back label, however we can create a different label die line should the design warrant that. Note this is just for the front label.
Should not have
• Difficult to read fonts or imagery that is not clear.
• Should look different to the Marlowe branded product range.

```html
<!DOCTYPE html>
<html lang="en">
<head>
<meta charset="utf-8">
<title>Brightcup Coffee Syrup – Hazelnut Front Label</title>
<link rel="stylesheet" href="https://fonts.googleapis.com/css2?family=Bebas+Neue&family=Oswald:wght@600&display=swap">
<style>
  :root {
    --brown: #6d2218;
    --ink: #111111;
    --paper: #ffffff;
    --backdrop: #ffffff;
  }
  * { margin: 0; padding: 0; box-sizing: border-box; }
  html, body {
    width: 1200px;
    height: 864px;
    overflow: hidden;
    background: var(--backdrop);
  }
  .canvas {
    position: relative;
    width: 1200px;
    height: 864px;
  }
  .label {
    position: absolute;
    left: 345px;
    top: 32px;
    width: 510px;
    height: 800px;
    background: var(--paper);
    border: 2px solid var(--brown);
    border-radius: 14px;
    overflow: hidden;
  }
  .label__stripes {
    position: absolute;
    left: 0;
    top: 32px;
    width: 100%;
    height: 34px;
  }
  .label__stripes span {
    display: block;
    height: 3px;
    margin-bottom: 7px;
    background: var(--brown);
  }
  .brand-tab {
    position: absolute;
    left: 184px;
    top: -2px;
    width: 138px;
    height: 126px;
    background: var(--brown);
    border-radius: 0 0 14px 14px;
    display: flex;
    align-items: center;
    justify-content: center;
  }
  .brand-tab__name {
    font-family: "Bebas Neue", sans-serif;
    font-size: 28px;
    letter-spacing: 1px;
    color: var(--paper);
  }
  .title {
    position: absolute;
    left: 0;
    width: 100%;
    text-align: center;
    font-family: "Bebas Neue", sans-serif;
    line-height: 1;
    white-space: nowrap;
  }
  .title--brand {
    top: 168px;
    font-size: 140px;
    color: var(--brown);
    letter-spacing: 1px;
  }
  .title--product {
    top: 302px;
    font-size: 96px;
    color: var(--ink);
    letter-spacing: 1px;
  }
  .hero-art {
    position: absolute;
    left: 95px;
    top: 425px;
    width: 316px;
    height: 164px;
  }
  .flavour {
    position: absolute;
    left: 84px;
    top: 643px;
    width: 335px;
    height: 49px;
    border-radius: 25px;
    background: var(--brown);
    color: var(--paper);
    font-family: "Oswald", sans-serif;
    font-weight: 600;
    font-size: 28px;
    letter-spacing: 1px;
    display: flex;
    align-items: center;
    justify-content: center;
  }
  .flavour__star {
    position: absolute;
    top: 656px;
    width: 22px;
    height: 22px;
  }
  .flavour__star--left { left: 52px; }
  .flavour__star--right { left: 431px; }
  .volume {
    position: absolute;
    left: 0;
    top: 746px;
    width: 100%;
    display: flex;
    justify-content: center;
    align-items: center;
    font-family: "Oswald", sans-serif;
    font-weight: 600;
    font-size: 26px;
    letter-spacing: 7px;
    color: var(--ink);
  }
  .volume__divider {
    width: 2px;
    height: 38px;
    background: var(--ink);
    margin: 0 22px 0 8px;
  }
</style>
</head>
<body>
<main class="canvas">
  <section class="label">
    <div class="label__stripes" aria-hidden="true">
      <span></span><span></span><span></span><span></span>
    </div>
    <div class="brand-tab">
      <span class="brand-tab__name">Brightcup</span>
    </div>

    <h1 class="title title--brand">BRIGHTCUP</h1>
    <h2 class="title title--product">COFFEE SYRUP</h2>

    <svg class="hero-art" role="img" aria-label="Illustration of three hazelnuts" viewBox="0 0 316 164">
      <defs>
        <linearGradient id="nut-tone" x1="0" y1="0" x2="0" y2="1">
          <stop offset="0" stop-color="#7a2a1e"/>
          <stop offset="1" stop-color="#6d2218"/>
        </linearGradient>
      </defs>
      <rect x="0" y="0" width="316" height="164" rx="60" fill="url(#nut-tone)"/>
    </svg>

    <svg class="flavour__star flavour__star--left" viewBox="0 0 24 24" aria-hidden="true">
      <polygon points="12,1 15,9 23,9 17,14 19,22 12,17 5,22 7,14 1,9 9,9" fill="#6d2218"/>
    </svg>
    <div class="flavour">HAZELNUT</div>
    <svg class="flavour__star flavour__star--right" viewBox="0 0 24 24" aria-hidden="true">
      <polygon points="12,1 15,9 23,9 17,14 19,22 12,17 5,22 7,14 1,9 9,9" fill="#6d2218"/>
    </svg>

    <p class="volume">
      <span class="volume__size">750 ML</span>
      <span class="volume__divider" aria-hidden="true"></span>
      <span class="volume__dose">15 ML / CUP</span>
    </p>
  </section>
</main>
</body>
</html>
```